Copperfox Billboard

Please design a billboard using my photos and logos.
For photo of truck please crop the truck itself out and not have the trees / dirt in photo.
Please put " Best Prices in Sevier County"
Please put " 30-yard Dumpsters Starting at 600.00"
Please put " 16-yard Dumpsters Starting at 300.0"
Please put " Delivery and Pickup 7 Days a week"
Billboard size will be 10 ft tall 30 ft wide

```html
<!DOCTYPE html>
<html lang="en">
<head>
<meta charset="utf-8">
<title>Copperfox Dumpsters Billboard</title>
<link rel="stylesheet" href="https://fonts.googleapis.com/css2?family=Lato:wght@400;700;900&display=swap">
<style>
  :root {
    --page: #ffffff;
    --ink-dark: #2b1b47;
    --brand-purple: #7d3f98;
    --band-white: #ffffff;
    --text-light: #ffffff;
    --photo-light: #eeeeef;
    --photo-mid: #d9d9dc;
  }
  * { margin: 0; padding: 0; box-sizing: border-box; }
  html, body {
    width: 955px;
    height: 1200px;
    overflow: hidden;
    background: var(--page);
    font-family: "Lato", Arial, sans-serif;
  }
  .canvas {
    position: relative;
    width: 955px;
    height: 1200px;
  }
  .billboard {
    position: absolute;
    left: 40px;
    top: 454px;
    width: 875px;
    height: 292px;
    background: var(--ink-dark);
    overflow: hidden;
    box-shadow: 0 6px 18px rgba(0, 0, 0, 0.28);
  }
  .billboard-shapes {
    position: absolute;
    inset: 0;
    width: 875px;
    height: 292px;
  }
  .brand-name {
    position: absolute;
    left: 29px;
    top: 27px;
    width: 228px;
    color: var(--text-light);
    font-weight: 900;
    font-size: 31px;
    line-height: 34px;
    letter-spacing: 0.5px;
  }
  .divider {
    position: absolute;
    left: 271px;
    top: 33px;
    width: 3px;
    height: 64px;
    background: var(--text-light);
  }
  .tagline {
    position: absolute;
    left: 285px;
    top: 33px;
    color: var(--text-light);
    font-size: 15.5px;
    line-height: 18.5px;
  }
  .tagline .strong { font-weight: 700; }
  .tagline .county { margin-top: 8px; }
  .offer {
    position: absolute;
    top: 124px;
    width: 218px;
    height: 93px;
    background: var(--brand-purple);
    border: 2px solid var(--text-light);
    border-radius: 8px;
    color: var(--text-light);
    font-weight: 700;
    padding: 10px 12px 0 12px;
  }
  .offer-30 { left: 29px; }
  .offer-16 { left: 259px; }
  .offer-size {
    font-size: 21.5px;
    line-height: 22px;
    white-space: nowrap;
  }
  .offer-price-row {
    display: flex;
    align-items: baseline;
    justify-content: space-between;
    white-space: nowrap;
  }
  .offer-lead { font-size: 21.5px; line-height: 22px; }
  .offer-price {
    font-size: 46px;
    line-height: 40px;
    font-weight: 900;
    letter-spacing: -1px;
  }
  .contact {
    position: absolute;
    left: 30px;
    top: 256px;
    display: flex;
    align-items: center;
    gap: 12px;
    color: var(--brand-purple);
    font-weight: 900;
    font-size: 20px;
    line-height: 24px;
    white-space: nowrap;
  }
  .contact-item { display: flex; align-items: center; gap: 3px; }
  .contact-item svg { width: 15px; height: 15px; flex: none; }
  .web .tld { font-weight: 400; }
</style>
</head>
<body>
<div class="canvas">
  <section class="billboard" aria-label="Copperfox Dumpsters billboard">
    <svg class="billboard-shapes" viewBox="0 0 875 292" aria-hidden="false">
      <defs>
        <linearGradient id="photoTone" x1="0" y1="0" x2="1" y2="1">
          <stop offset="0" stop-color="var(--photo-light)"/>
          <stop offset="0.55" stop-color="#c9c9cf"/>
          <stop offset="1" stop-color="#4a3368"/>
        </linearGradient>
      </defs>
      <polygon class="accent-triangle" points="466,0 636,0 552,142" fill="var(--brand-purple)"/>
      <polygon class="accent-stripe" points="642,0 648,0 566,138 560,138" fill="var(--band-white)"/>
      <polygon class="truck-photo" role="img" aria-label="Photo of a white roll-off truck carrying a purple dumpster, cut out on a light background"
               points="652,0 875,0 875,292 496,292 540,190 572,138" fill="url(#photoTone)"/>
      <polygon class="contact-band" points="0,245 450,245 473,292 0,292" fill="var(--band-white)"/>
    </svg>

    <div class="brand-name">Copperfox<br>Dumpsters</div>
    <div class="divider"></div>
    <div class="tagline">
      <div>Delivery and Pickup</div>
      <div class="strong">7 Days a week</div>
      <div class="county">Best Prices in Sevier County</div>
    </div>

    <div class="offer offer-30">
      <div class="offer-size">30-yard Dumpsters</div>
      <div class="offer-price-row">
        <span class="offer-lead">Starting at</span>
        <span class="offer-price">600</span>
      </div>
    </div>
    <div class="offer offer-16">
      <div class="offer-size">16-yard Dumpsters</div>
      <div class="offer-price-row">
        <span class="offer-lead">Starting at</span>
        <span class="offer-price">300</span>
      </div>
    </div>

    <div class="contact">
      <span class="contact-item phone">
        <svg viewBox="0 0 24 24" aria-hidden="true"><path fill="var(--ink-dark)" d="M6.6 10.8a15.2 15.2 0 0 0 6.6 6.6l2.2-2.2a1 1 0 0 1 1-.25 11.4 11.4 0 0 0 3.6.57 1 1 0 0 1 1 1V20a1 1 0 0 1-1 1A17 17 0 0 1 3 4a1 1 0 0 1 1-1h3.5a1 1 0 0 1 1 1c0 1.25.2 2.45.57 3.6a1 1 0 0 1-.25 1z"/></svg>
        865-555-0142
      </span>
      <span class="contact-item web">
        <svg viewBox="0 0 24 24" aria-hidden="true"><circle cx="12" cy="12" r="9.5" fill="none" stroke="var(--ink-dark)" stroke-width="2"/><ellipse cx="12" cy="12" rx="4" ry="9.5" fill="none" stroke="var(--ink-dark)" stroke-width="1.6"/><line x1="2.5" y1="12" x2="21.5" y2="12" stroke="var(--ink-dark)" stroke-width="1.6"/></svg>
        <span>copperfoxdumpsters<span class="tld">.com</span></span>
      </span>
    </div>
  </section>
</div>
</body>
</html>
```